Childrens Business Card Design Project

We have an existing logo attached which we'd like to use as part of our new business card design.

The design needs to be relatively gender neutral and contain bright colours.

In terms of look and feel think:

Fun, Modern, Quality (as opposed to cheap!) and of course Party!

Single or double sided - i am not decided on either one yet - ideally i'd like to see designs for both because if you think stylistically it would benefit having two sides then please try it out!

I think the challenge here is finding a really good background colour (if you think it needs one) and also choosing an eye grabbing text that compliments the existing logo - do that an you are onto a winner! I have another image for the business (which i have attached) which uses stripes so i am keen to see a design that incorporates this to tie in all my collateral.

The copy required is as follows (not necesarily in this order)

Bookings/Enquiries:

Tilda

T: 0498 765 210
E: enquiries@brixtopia.com.au

ABN: 43 527 806 214

Any feedback on text is welcomed - please message me or add to the discussion.

Reason: Hi All, I have received some promising designs, but overall i am not impressed with the quality of the work so have extended the deadline as this project has been committed. I will aim to attach some business card examples to the brief tomorrow to give further guidance as a whole but please do not submit any designs on a generic background that are not related to the theme, have been carelessly placed with overlapping elements - it just looks sloppy. For those who have read the brief an incorporated stripes or even spots this is on target as it convey's a party theme, however please work on getting the colours for the contact details by either a bold solid strip to highlight or some other way to frame it. When it comes to the logo, some people have removed the characters all together and changed the colour of the wording - this is fine. Also feel free to balloons starts - but keep it classy and watch your placement of these. I hope this helps and for the designs i would like to see revisions for i will aim to get back to you individually over the next day or so. Many thanks all.

Target Market(s)

Mothers in the suburbs of Australia with a disposal able income, children aged between 1-7 years old.

Industry/Entity Type

Business

Requirements
Must have
• The font and wording positioning must compliment the logo.

```html
<!DOCTYPE html>
<html lang="en">
<head>
<meta charset="utf-8">
<title>Brixtopia Business Card</title>
<link rel="stylesheet" href="https://fonts.googleapis.com/css2?family=Ubuntu:wght@400;500;700&display=swap">
<style>
  :root {
    --page: #ece8e2;
    --purple-deep: #9a55c8;
    --purple-light: #ac72d6;
    --purple-text: #8d44c4;
    --cream: #f6f2c8;
    --cream-edge: #e7e0a6;
    --peach: #f7a37c;
    --white: #ffffff;
    --grey: #9c96a6;
    --figure: #e7c7ec;
  }
  * { margin: 0; padding: 0; box-sizing: border-box; }
  html, body {
    width: 1200px;
    height: 1023px;
    overflow: hidden;
    background: var(--page);
  }
  .card {
    position: absolute;
    left: 150px;
    top: 251px;
    width: 900px;
    height: 520px;
    border-radius: 28px;
    overflow: hidden;
    box-shadow: 0 14px 40px rgba(60, 40, 80, 0.18);
    font-family: "Ubuntu", sans-serif;
  }
  .card-art {
    position: absolute;
    inset: 0;
  }
  .characters {
    position: absolute;
    left: 70px;
    top: 110px;
    width: 420px;
    height: 120px;
    border-radius: 60px;
    background: linear-gradient(90deg, #f2b3cf, #f5e0a0, #9fd6ef, #f2b3cf);
    opacity: 0.75;
  }
  .brand {
    position: absolute;
    left: 70px;
    top: 250px;
    width: 420px;
    text-align: center;
  }
  .brand-name {
    font-size: 66px;
    font-weight: 500;
    letter-spacing: 6px;
    color: var(--cream);
    line-height: 1;
  }
  .brand-tagline {
    margin-top: 14px;
    font-size: 22px;
    font-weight: 400;
    letter-spacing: 5px;
    color: var(--white);
  }
  .contact {
    position: absolute;
    left: 590px;
    top: 150px;
    width: 290px;
  }
  .contact-name {
    font-size: 36px;
    font-weight: 700;
    letter-spacing: 1px;
    color: var(--peach);
  }
  .contact-line {
    margin-top: 12px;
    font-size: 30px;
    font-weight: 700;
    color: var(--purple-text);
  }
  .contact-email {
    font-size: 21px;
    margin-top: 16px;
  }
  .abn {
    position: absolute;
    right: 34px;
    bottom: 30px;
    font-size: 19px;
    font-weight: 400;
    color: var(--grey);
    letter-spacing: 1px;
  }
</style>
</head>
<body>
  <div class="card">
    <svg class="card-art" width="900" height="520" viewBox="0 0 900 520" aria-hidden="true">
      <defs>
        <pattern id="party-stripes" width="44" height="44" patternUnits="userSpaceOnUse">
          <rect width="22" height="44" fill="var(--purple-deep)"/>
          <rect x="22" width="22" height="44" fill="var(--purple-light)"/>
        </pattern>
      </defs>
      <rect width="900" height="520" fill="url(#party-stripes)"/>
      <path d="M600 0 C 520 140, 520 380, 600 520 L900 520 L900 0 Z" fill="var(--purple-deep)"/>
      <path d="M618 0 C 540 140, 540 380, 618 520 L900 520 L900 0 Z" fill="var(--cream)"/>
      <path d="M618 0 C 540 140, 540 380, 618 520" fill="none" stroke="var(--cream-edge)" stroke-width="3"/>
    </svg>

    <div class="characters" role="img" aria-label="Illustrated party characters in costume: a fairy, a clown and a pirate"></div>

    <div class="brand">
      <div class="brand-name">Brixtopia</div>
      <div class="brand-tagline">Kids Parties &amp; Events</div>
    </div>

    <div class="contact">
      <div class="contact-name">TILDA</div>
      <div class="contact-line">0498 765 210</div>
      <div class="contact-line contact-email">enquiries@brixtopia.com.au</div>
    </div>

    <div class="abn">ABN: 43 527 806 214</div>
  </div>
</body>
</html>
```